Wix site for a family history research service / genealogist

Design a Wix website for a genealogy/family history research business.

The colour scheme and logo exist and the main imagery has been selected and purchased. The main emotion I'd like the website to convey is "looking up" - like looking up your family tree, looking up a DNA helix, looking up to your parents, grandparents etc. I want the vibe to be one that is enthusiastic about the potential discoveries in your family's history you can make on my website. My service is to the general public, but the main target group are older people 50+ in Australia (I advertise in retirement homes, on golf courses etc.).
I'd like the website to be
- friendly, warm, approachable, trustworthy and open in terms of it's feel
- easy to read, understand and navigate for older people (this is important)
- feature a "language switch" that allows for 3 languages. Ideally pre-selected by geographic origin of visitor.
- Show clear pathways to action (contact or purchase)
- Has a simply shopping cart function that connects to PayPal

The website sections are as follows:
1. A general "Home" page or section
2. About us/me
3. Services (there will be an initial 4 products/services)
3.1 Traditional genealogy (2 products)
3.2 DNA-based ancestry tracing (2 products)
4. Case studies (initially 2)
5. Contact
(The headings are only indicative at this stage)
There is no pre-existing content yet. I'd like to work with lorem ipsum at the beginning. Some more imagery may have to be acquired, I am expecting that.
So far there is only a Facebook page https://www.examplesocial.test/profile.php?id=48305716294082

Target Market(s)

Older people in Australia, more males than females

Industry/Entity Type

Personal services - Genealogy

Font styles to use
Serif
Decorative

Colors

Designer to choose colors to be used in the design.

Requirements
Must have
• Feel warm, feel trustworthy, clear call to action
Should not have
• Too small writing, confusing imagery

```html
<!DOCTYPE html>
<html lang="en">
<head>
<meta charset="utf-8">
<title>Thomas R. Whitfield – Family History Research Office</title>
<link href="https://fonts.googleapis.com/css2?family=Cinzel:wght@400;500;600&family=Raleway:wght@400;500&display=swap" rel="stylesheet">
<style>
:root{
  --green:#0b7a3a;
  --green-dark:#05612c;
  --green-bright:#0aa34a;
  --green-pale:#cfe6d7;
  --card:#eef0ee;
  --band:#f4f5f4;
  --text:#333;
  --muted:#8a8a8a;
  --black:#000;
  --white:#fff;
}
*{margin:0;padding:0;box-sizing:border-box}
html,body{width:1200px;height:3987px;overflow:hidden}
body{position:relative;background:var(--white);font-family:'Raleway',sans-serif;color:var(--text)}
.abs{position:absolute}
.serif{font-family:'Cinzel',serif}
.title{font-family:'Cinzel',serif;font-size:36px;font-weight:500;color:var(--green-dark);letter-spacing:1px}
.title span{color:var(--green-bright)}
.body{font-size:14.5px;line-height:32.5px;color:var(--text)}
.divider{display:flex;align-items:center;gap:18px}
.divider i{display:block;width:28px;height:28px;border-radius:50%;background:var(--green-pale);border:2px solid var(--green-bright)}
.divider b{display:block;width:48px;height:2px;background:var(--green-dark)}
.pill{border:1.5px solid var(--green);border-radius:20px;color:var(--green-dark);font-family:'Cinzel',serif;font-size:15px;display:flex;align-items:center;justify-content:center;gap:8px}
.btn-solid{background:var(--green-dark);color:var(--white);border-radius:24px;font-family:'Cinzel',serif;font-weight:600;font-size:15px;display:flex;align-items:center;justify-content:center}
.btn-line{border:1.5px solid var(--green);border-radius:24px;color:var(--green-dark);font-family:'Cinzel',serif;font-size:15px;display:flex;align-items:center;justify-content:center;background:transparent}
/* header */
.nav{top:116px;left:0;width:1200px;display:flex;justify-content:center;gap:0}
.nav a{position:absolute;font-family:'Cinzel',serif;font-size:14px;color:#444;text-decoration:none;top:0}
.nav a.active{color:var(--green-bright)}
/* hero */
.hero-img{top:159px;left:0;width:1200px;height:627px;background:linear-gradient(160deg,#3f5a22 0%,#6f8a3a 35%,#4b6a2a 60%,#2f4a1a 100%)}
.hero-circle{left:139px;top:240px;width:418px;height:418px;border-radius:50%;background:var(--green);border:3px solid var(--green-bright);text-align:center;color:var(--white)}
.card{background:var(--card);border-radius:14px}
.card h3{font-family:'Cinzel',serif;font-weight:500;font-size:25px;color:var(--green-dark);letter-spacing:1px}
.case{border:1.5px solid #e6e6e6;border-radius:16px;background:var(--white);overflow:hidden;text-align:center}
.case h3{font-family:'Cinzel',serif;font-weight:500;font-size:19px;line-height:39px;color:var(--green);letter-spacing:.5px}
.case .photo{position:absolute;left:9px;top:11px;width:450px;height:265px;border-radius:12px}
.case .go{position:absolute;right:-1px;bottom:-1px;width:72px;height:57px;background:var(--green-dark);border-radius:48px 0 16px 0;display:flex;align-items:center;justify-content:center}
.field{border:1.5px solid #d9d9d9;border-radius:3px;font-size:13px;color:#aaa;padding:10px 14px}
.foot h4{font-family:'Cinzel',serif;font-weight:500;font-size:22px;color:var(--green-bright);letter-spacing:1px}
.foot a{display:block;color:var(--white);text-decoration:none;font-size:17px;line-height:44px}
.pay{width:32px;height:18px;border-radius:3px;background:#ddd}
</style>
</head>
<body>

<!-- Header -->
<div class="abs pill" style="left:111px;top:43px;width:73px;height:30px">EN
  <svg width="10" height="6" viewBox="0 0 10 6"><path d="M0 0h10L5 6z" fill="#05612c"/></svg></div>
<div class="abs" style="left:458px;top:25px;display:flex;align-items:center;gap:14px">
  <div style="width:68px;height:68px;border-radius:50%;background:var(--green)"></div>
  <div class="serif" style="color:var(--green);font-size:20px;font-weight:600;line-height:20px">THOMAS R. WHITFIELD<br><span style="font-size:10px;font-weight:500;letter-spacing:.5px">FAMILY HISTORY RESEARCH OFFICE</span></div>
</div>
<div class="abs pill" style="left:996px;top:43px;width:92px;height:30px">CART
  <svg width="18" height="16" viewBox="0 0 18 16" fill="none" stroke="#05612c" stroke-width="1.4"><path d="M1 1h3l2 9h9l2-6H5"/><circle cx="7" cy="14" r="1.2"/><circle cx="14" cy="14" r="1.2"/></svg></div>
<nav class="abs nav">
  <a class="active" style="left:316px">HOME</a>
  <a style="left:402px">ABOUT ME</a>
  <a style="left:519px">OUR SERVICES</a>
  <a style="left:662px">CASE STUDY</a>
  <a style="left:790px">CONTACT US</a>
</nav>

<!-- Hero -->
<div class="abs hero-img" role="img" aria-label="Child sitting high in a large moss-covered tree, seen looking up through the branches"></div>
<svg class="abs" style="left:0;top:660px" width="1200" height="130" viewBox="0 0 1200 130">
  <path d="M0 10 Q600 190 1200 10 L1200 130 L0 130Z" fill="#fff"/>
  <path d="M0 10 Q600 190 1200 10 Q600 150 0 10Z" fill="#0b7a3a"/>
</svg>
<div class="abs hero-circle">
  <div class="serif" style="margin-top:110px;font-size:26px;letter-spacing:1px">DISCOVER YOUR ROOTS,</div>
  <div class="serif" style="margin-top:12px;font-size:21px;letter-spacing:1px">UNCOVER YOUR STORY</div>
  <p style="margin:20px auto 0;width:340px;font-size:14px;line-height:32.5px">Lorem ipsum dolor sit amet, consectetur adipiscing elit, sed do eiusmod tempor incididunt ut labore et dolore magna aliqua.</p>
  <div class="btn-solid" style="background:#fff;color:var(--green-dark);font-weight:500;width:158px;height:41px;margin:26px auto 0;font-size:14px">PURCHASE NOW</div>
</div>

<!-- Services -->
<h2 class="abs title" style="left:111px;top:860px">OUR <span>SERVICES</span></h2>
<div class="abs divider" style="left:111px;top:920px"><i></i><b></b></div>
<p class="abs body" style="left:111px;top:975px;width:440px">Lorem ipsum dolor sit amet, consectetur adipiscing elit, sed do eiusmod tempor incididunt ut labore et dolore magna aliqua.</p>

<div class="abs card" style="left:111px;top:1079px;width:468px;height:355px">
  <svg style="position:absolute;left:34px;top:32px" width="66" height="66" viewBox="0 0 66 66" fill="none" stroke="#0b7a3a" stroke-width="2.5"><circle cx="33" cy="11" r="8"/><circle cx="12" cy="22" r="8"/><circle cx="54" cy="22" r="8"/><circle cx="12" cy="44" r="8"/><circle cx="54" cy="44" r="8"/><path d="M33 19v45M20 25l13 12 13-12M20 44l13 8 13-8M22 64h22"/></svg>
  <h3 style="position:absolute;left:35px;top:124px">TRADITIONAL GENEALOGY</h3>
  <p class="body" style="position:absolute;left:35px;top:167px;width:410px">Lorem ipsum dolor sit amet, consectetur adipiscing elit, sed do eiusmod tempor incididunt ut labore et dolore magna aliqua enim ad minim veniam.</p>
  <div class="btn-line" style="position:absolute;left:35px;top:285px;width:138px;height:41px">LEARN MORE</div>
</div>
<div class="abs card" style="left:623px;top:870px;width:467px;height:484px">
  <svg style="position:absolute;left:34px;top:30px" width="66" height="66" viewBox="0 0 66 66" fill="none" stroke="#0b7a3a" stroke-width="2.5"><path d="M8 2c24 18 24 44 0 62M34 2C10 20 10 46 34 64M12 14h18M12 50h18"/><circle cx="36" cy="34" r="11"/><path d="M44 42l18 18"/></svg>
  <h3 style="position:absolute;left:34px;top:125px">DNA-BASED ANCESTRY TRACING</h3>
  <p class="body" style="position:absolute;left:34px;top:167px;width:410px">Lorem ipsum dolor sit amet, consectetur adipiscing elit, sed do eiusmod tempor incididunt ut labore et dolore magna aliqua enim ad minim veniam quis nostrud exercitation ullamco laboris nisi ut aliquip ex ea commodo consequat. Duis aute irure dolor in reprehenderit in voluptate velit esse cillum dolore eu fugiat nulla pariatur.</p>
  <div class="btn-line" style="position:absolute;left:34px;top:400px;width:138px;height:41px">LEARN MORE</div>
</div>
<svg class="abs" style="left:527px;top:1065px" width="68" height="68" viewBox="0 0 68 68" fill="#d8d8d8"><g transform="translate(34 34)"><circle cx="0" cy="-28" r="4"/><circle cx="20" cy="-20" r="4"/><circle cx="28" cy="0" r="4"/><circle cx="20" cy="20" r="4"/><circle cx="0" cy="28" r="4"/><circle cx="-20" cy="20" r="4"/><circle cx="-28" cy="0" r="4"/><circle cx="-20" cy="-20" r="4"/></g></svg>
<svg class="abs" style="left:1038px;top:852px" width="68" height="68" viewBox="0 0 68 68" fill="#d8d8d8"><g transform="translate(34 34)"><circle cx="0" cy="-28" r="4"/><circle cx="20" cy="-20" r="4"/><circle cx="28" cy="0" r="4"/><circle cx="20" cy="20" r="4"/><circle cx="0" cy="28" r="4"/><circle cx="-20" cy="20" r="4"/><circle cx="-28" cy="0" r="4"/><circle cx="-20" cy="-20" r="4"/></g></svg>

<!-- About -->
<svg class="abs" style="left:0;top:1470px" width="1200" height="620" viewBox="0 0 1200 620">
  <path d="M0 10 Q600 -20 1200 10 L1200 614 L0 614Z" fill="#f4f5f4"/>
  <path d="M105 34 Q600 120 1110 34 Q600 92 105 34Z" fill="#0aa34a"/>
</svg>
<h2 class="abs title" style="left:110px;top:1603px">ABOUT <span>ME</span></h2>
<div class="abs divider" style="left:111px;top:1663px"><i></i><b></b></div>
<p class="abs body" style="left:110px;top:1722px;width:545px">Lorem ipsum dolor sit amet, consectetur adipiscing elit, sed do eiusmod tempor incididunt ut labore et dolore magna aliqua enim ad minim veniam quis nostrud exercitation ullamco laboris nisi ut aliquip ex ea commodo consequat. Duis aute irure dolor in reprehenderit in voluptate velit esse cillum dolore eu fugiat nulla pariatur dolor sit amet, consectetur adipiscing elit, sed do eiusmod tempor incididunt ut labore et dolore magna aliqua enim ad minim veniam quis nostrud exercitation ullamco laboris nisi ut aliquip ex ea commodo consequat.</p>
<div class="abs btn-solid" style="left:110px;top:1981px;width:142px;height:41px">LEARN MORE</div>
<div class="abs" style="left:728px;top:1656px;width:356px;height:356px;border-radius:50%;border:10px solid #b9dcc6"></div>
<div class="abs" role="img" aria-label="Portrait of the researcher in a beige jacket and blue shirt" style="left:782px;top:1613px;width:285px;height:350px;background:linear-gradient(180deg,#e9ece9 0%,#b8a590 45%,#7a6d60 70%,#2c4c8c 100%)"></div>
<svg class="abs" style="left:738px;top:1628px" width="36" height="36" viewBox="0 0 36 36"><clipPath id="c1"><circle cx="18" cy="18" r="17"/></clipPath><g clip-path="url(#c1)" stroke="#666" stroke-width="1.5"><path d="M0 4h36M0 9h36M0 14h36M0 19h36M0 24h36M0 29h36M0 34h36"/></g></svg>
<svg class="abs" style="left:1057px;top:1972px" width="36" height="36" viewBox="0 0 36 36"><clipPath id="c2"><circle cx="18" cy="18" r="17"/></clipPath><g clip-path="url(#c2)" stroke="#666" stroke-width="1.5"><path d="M0 4h36M0 9h36M0 14h36M0 19h36M0 24h36M0 29h36M0 34h36"/></g></svg>

<!-- Case studies -->
<h2 class="abs title" style="left:0;top:2158px;width:1200px;text-align:center">CASE <span>STUDIES</span></h2>
<div class="abs divider" style="left:519px;top:2217px"><b></b><i></i><b></b></div>

<div class="abs case" style="left:116px;top:2294px;width:468px;height:523px">
  <div class="photo" role="img" aria-label="Vintage family tree painting with portrait medallions on its branches" style="background:linear-gradient(160deg,#9c8a62,#6b5a3c 50%,#b4a27a)"></div>
  <h3 style="position:absolute;left:20px;top:305px;width:428px">THE DISCOVERY OF FAMILY CONNECTIONS ACROSS GENERATIONS</h3>
  <p class="body" style="position:absolute;left:20px;top:393px;width:428px;font-size:14px">Lorem ipsum dolor sit amet, consectetur adipiscing elit, sed do eiusmod tempor incididunt ut labore et dolore magna aliqua enim ad minim veniam quis nostrud.</p>
  <div class="go"><svg width="26" height="14" viewBox="0 0 26 14" fill="none" stroke="#fff" stroke-width="2"><path d="M0 7h24M18 1l6 6-6 6"/></svg></div>
</div>
<div class="abs case" style="left:616px;top:2294px;width:468px;height:523px">
  <div class="photo" role="img" aria-label="Father and two children studying a DNA helix model at a desk" style="background:linear-gradient(160deg,#f2f2ef,#d9d4cc 50%,#b9a996)"></div>
  <h3 style="position:absolute;left:20px;top:305px;width:428px">RECONNECTING WITH LOST ANCESTORS IN AUSTRALIA</h3>
  <p class="body" style="position:absolute;left:20px;top:393px;width:428px;font-size:14px">Lorem ipsum dolor sit amet, consectetur adipiscing elit, sed do eiusmod tempor incididunt ut labore et dolore magna aliqua enim ad minim veniam quis nostrud.</p>
  <div class="go"><svg width="26" height="14" viewBox="0 0 26 14" fill="none" stroke="#fff" stroke-width="2"><path d="M0 7h24M18 1l6 6-6 6"/></svg></div>
</div>

<!-- Contact -->
<div class="abs" style="left:111px;top:2904px;width:977px;height:502px;border:1.5px solid #e6e6e6;border-radius:16px"></div>
<h2 class="abs title" style="left:162px;top:2944px">CONTACT <span>US</span></h2>
<div class="abs divider" style="left:163px;top:3004px"><i></i><b></b></div>
<div class="abs field" style="left:163px;top:3074px;width:184px;height:36px">First Name</div>
<div class="abs field" style="left:368px;top:3074px;width:185px;height:36px">Last Name</div>
<div class="abs field" style="left:163px;top:3138px;width:184px;height:36px">Email Address</div>
<div class="abs field" style="left:368px;top:3138px;width:185px;height:36px">Phone Number</div>
<div class="abs field" style="left:163px;top:3204px;width:390px;height:70px">Type Your Message</div>
<div class="abs btn-solid" style="left:163px;top:3310px;width:150px;height:40px">SEND MESSAGE</div>
<div class="abs" role="img" aria-label="Street map showing the office location with a red pin" style="left:624px;top:2924px;width:446px;height:458px;border-radius:14px;background:linear-gradient(135deg,#e4e6e4,#d3d6d3 50%,#e4e6e4)"></div>
<svg class="abs" style="left:872px;top:3224px" width="18" height="26" viewBox="0 0 18 26"><path d="M9 0a9 9 0 0 1 9 9c0 7-9 17-9 17S0 16 0 9a9 9 0 0 1 9-9z" fill="#e02020"/><circle cx="9" cy="9" r="3.5" fill="#fff"/></svg>

<!-- Footer -->
<svg class="abs" style="left:0;top:3480px" width="1200" height="507" viewBox="0 0 1200 507">
  <path d="M0 130 Q600 -100 1200 130 L1200 507 L0 507Z" fill="#000"/>
  <path d="M0 130 Q600 -100 1200 130 Q600 -80 0 130Z" fill="#0b7a3a"/>
</svg>
<div class="abs" style="left:166px;top:3618px;width:170px;height:170px;border-radius:50%;border:4px solid #fff"></div>
<div class="abs serif" style="left:110px;top:3800px;width:280px;text-align:center;color:#fff;font-size:20px;line-height:20px">THOMAS R. WHITFIELD<br><span style="font-size:10px">FAMILY HISTORY RESEARCH OFFICE</span></div>
<div class="abs foot" style="left:516px;top:3614px"><h4>QUICK LINKS</h4>
  <div style="margin-top:14px"><a>Home</a><a>About Me</a><a>Services</a><a>Case Study</a><a>Contact</a></div></div>
<div class="abs foot" style="left:808px;top:3614px"><h4>SERVICES</h4>
  <div style="margin-top:14px"><a>Traditional genealogy (2)</a><a>DNA-based ancestry tracing (2)</a></div></div>
<div class="abs" style="left:138px;top:3924px;width:924px;height:1px;background:#333"></div>
<div class="abs" style="left:140px;top:3946px;color:#fff;font-size:14px">@2025 Copyrights - All Rights Reserved</div>
<div class="abs" style="left:860px;top:3946px;display:flex;gap:11px"><div class="pay"></div><div class="pay"></div><div class="pay"></div><div class="pay"></div><div class="pay"></div></div>

</body>
</html>
```